Modern Homepage Design for brenvik.nl – Fish & Chicken Food Webshop

Brenvik.nl is an online store that sells fish and chicken food. The design should be visually appealing, easy to navigate, and optimized for e-commerce. We want a layout that helps customers quickly find what they need and encourages them to explore our products.
A good example of the style and structure we like is dierkamp.nl – clean layout, clear product focus, and user-friendly navigation.
Brand Colors (must be used):
Orange: #f7a441
Dark Gray: #3c3c3b
White: #ffffff
Please use these colors consistently throughout the design.
Homepage Requirements:
The homepage should include the following sections:
Main Slider / Hero Banner
A large, eye-catching slider at the top of the page to highlight promotions or featured categories.
Category Blocks
A section with clear, clickable blocks or tiles that link to main product categories (e.g., Fish Food, Chicken Food, Accessories).
Featured Products
A section showcasing selected or best-selling products.
Special Offers / Promotions
A space to highlight current deals or limited-time offers.
Three Banners in a Row
A section with three horizontal banners side by side, which can be used for promotions, shipping info, or other key messages.
Unique Selling Points (USPs)
A section that briefly explains what makes our store different (e.g., fast delivery, high-quality feed, trusted by professionals).
SEO Content Block
A short paragraph of text for SEO purposes (use Lorem Ipsum for dummy content).
Footer Design
Include space for contact information, navigation links, and social media.
Design Notes:
The design must be responsive and mobile-friendly.
Focus on clean layout, good spacing, and easy navigation.
Use modern fonts and a clear visual hierarchy.
We are only looking for the homepage design at this stage, but we may work with the selected designer on additional pages later.
Deliverables:
Homepage design in layered PSD, Figma, or Adobe XD format
Any fonts and assets used
Preview images/mockups
We look forward to seeing your ideas and working with a designer who can bring our brand to life with a fresh and functional homepage design.
Let us know if you have any questions.
Hobby Animal Keepers, Pet Owners
Animal Nutrition & Feed
2 page

```html
<!DOCTYPE html>
<html lang="nl">
<head>
<meta charset="utf-8">
<title>Brenvik.nl – Vis- en kippenvoer</title>
<link href="https://fonts.googleapis.com/css2?family=Nunito:wght@400;600;700;800&display=swap" rel="stylesheet">
<style>
:root{
  --orange:#f7a441;
  --dark:#3c3c3b;
  --white:#ffffff;
  --peach:#fdf1e2;
  --peach-2:#fde6c8;
  --green:#1f8a1c;
  --green-text:#2e7d1e;
  --red:#e5482b;
  --muted:#6d6d6b;
  --line:#e7e2da;
  --lav:#efeff8;
  --lav-line:#b9b9d6;
  --blue:#2f6fd6;
}
*{box-sizing:border-box;margin:0;padding:0}
html,body{width:1200px;height:3813px;overflow:hidden}
body{font-family:"Nunito",sans-serif;color:var(--dark);background:var(--white);position:relative}
.abs{position:absolute}
a{color:inherit;text-decoration:none}
.btn{display:inline-flex;align-items:center;justify-content:center;background:var(--orange);color:var(--white);font-weight:700;border-radius:999px}
.btn-outline{display:inline-flex;align-items:center;justify-content:center;border:1px solid var(--orange);color:var(--orange);border-radius:999px;font-size:10px;font-weight:600;background:var(--white)}
.ph{display:block}
.stars{color:var(--orange);font-size:12px;letter-spacing:1px}
.stars small{color:#9a9a98;font-size:7px;letter-spacing:0;margin-left:4px}
.badge{display:inline-block;background:var(--green);color:var(--white);font-size:8px;font-weight:700;padding:3px 9px;border-radius:999px}

.topbar{top:0;left:0;width:1200px;height:32px;background:var(--orange);color:var(--white);font-size:11px;font-weight:700;text-align:center;line-height:32px}
.header{top:32px;left:0;width:1200px;height:128px;background:var(--white);box-shadow:0 2px 6px rgba(0,0,0,.06);z-index:2}
.logo{display:flex;align-items:center;gap:8px;font-weight:800;color:var(--dark)}
.logo .dot{width:28px;height:28px;border-radius:50%;background:var(--orange)}
.header .logo{position:absolute;left:117px;top:14px;font-size:34px}
.search{position:absolute;left:366px;top:14px;width:540px;height:38px;border-radius:999px;background:#f1f0ee;font-size:11px;color:#9a9a98;padding-left:16px;line-height:38px}
.search svg{position:absolute;right:16px;top:10px}
.hicons{position:absolute;left:940px;top:12px;display:flex;gap:18px}
.hicon{display:flex;flex-direction:column;align-items:center;font-size:9px;color:var(--dark);gap:4px}
.nav{position:absolute;left:117px;top:92px;display:flex;font-size:13px;font-weight:600}
.nav a{position:absolute;white-space:nowrap}
.header .shop{position:absolute;left:977px;top:79px;width:106px;height:31px;font-size:13px}

.hero{top:160px;left:0;width:1200px;height:402px;background:var(--peach)}
.hero-card{position:absolute;left:117px;top:25px;width:966px;height:314px;background:var(--white);border-radius:20px;overflow:hidden}
.hero-text{position:absolute;left:33px;top:30px;width:300px}
.hero-text h1{font-size:31px;font-weight:800;line-height:42px;margin-top:12px}
.hero-text p{font-size:12px;line-height:18px;margin-top:16px}
.hero-text .btn{margin-top:20px;width:106px;height:33px;font-size:13px}
.hero-img{position:absolute;left:336px;top:0;width:564px;height:314px;background:linear-gradient(135deg,#dcdcdc,#f2f2f2 55%,#e0e6ea);clip-path:polygon(14% 0,100% 0,100% 100%,0 100%)}
.hero-stripe{position:absolute;left:320px;top:0;width:110px;height:314px;background:var(--peach-2);clip-path:polygon(40% 0,100% 0,60% 100%,0 100%)}
.hero-band{position:absolute;right:0;top:0;width:66px;height:314px;background:var(--green);border-top-left-radius:40px}
.hero-band span{position:absolute;left:50%;top:50%;transform:translate(-50%,-50%) rotate(-90deg);color:var(--white);font-size:27px;font-weight:800;white-space:nowrap}
.dots{position:absolute;top:364px;left:537px;display:flex;gap:16px}
.dots i{width:12px;height:12px;border-radius:50%;background:#e0d6ca}
.dots i.on{background:var(--orange)}

.sec-title{font-size:23px;font-weight:700}
.sec-sub{font-size:11px;margin-top:6px}
.see-all{position:absolute;right:0;font-size:12px;font-weight:600;text-decoration:underline;display:flex;align-items:center;gap:6px}

.cats{top:626px;left:117px;width:966px}
.cats-head{text-align:center}
.cat-row{position:absolute;top:84px;left:0;display:flex;gap:15px}
.cat{width:312px;height:218px;background:var(--white);border-radius:10px;box-shadow:0 3px 10px rgba(0,0,0,.1);overflow:hidden;position:relative}
.cat .ph{height:112px}
.cat h3{font-size:14px;font-weight:800;margin:14px 16px 0}
.cat p{font-size:10px;margin:6px 16px 0;line-height:14px;color:#444}
.cat .btn-outline{position:absolute;right:17px;bottom:14px;width:106px;height:24px}

.bundles{top:990px;left:117px;width:966px}
.bundle-row{position:absolute;top:98px;display:flex;gap:14px}
.bundle{width:312px;height:164px;border-radius:10px;position:relative;overflow:hidden}
.bundle h3{position:absolute;left:14px;top:30px;font-size:16px;font-weight:800;line-height:21px;width:150px;z-index:1}
.bundle p{position:absolute;left:14px;top:86px;font-size:10px;line-height:12px;width:110px}
.bundle .ph{position:absolute;right:14px;top:14px;width:128px;height:130px;border-radius:8px}
.bundle .go{position:absolute;right:10px;bottom:12px;width:36px;height:36px;border-radius:50%;background:var(--orange);display:flex;align-items:center;justify-content:center}
.b1{background:#fde0bd}.b1 h3,.b1 p{color:var(--orange)}
.b2{background:#e3e9ee}
.b3{background:#e5f2d8}.b3 h3,.b3 p{color:var(--green-text)}

.rated{top:1314px;left:0;width:1200px;height:542px;background:var(--peach)}
.rated-in{position:absolute;left:117px;top:64px;width:966px}
.prod-row{position:absolute;top:65px;left:0;display:flex;gap:13px}
.prod{width:232px;height:324px;background:var(--white);border-radius:10px;box-shadow:0 2px 8px rgba(0,0,0,.08);overflow:hidden;position:relative}
.prod .ph{height:184px}
.prod .badge{position:absolute;left:8px;top:8px}
.prod .body{padding:10px 12px}
.prod h4{font-size:13px;font-weight:700;line-height:17px}
.prod .desc{font-size:8px;color:#555;margin-top:4px;line-height:10px}
.price{color:var(--green-text);font-weight:800;font-size:17px}
.price small{font-size:6px;color:#999;font-weight:400;margin-left:3px}
.prod .price{position:absolute;left:12px;bottom:46px}
.prod .btn{position:absolute;right:12px;bottom:12px;width:114px;height:25px;font-size:10px}
.arrow-btn{position:absolute;width:40px;height:40px;border-radius:50%;background:var(--orange);display:flex;align-items:center;justify-content:center}
.track{position:absolute;left:114px;top:490px;width:971px;height:4px;background:#e8ddd0;border-radius:2px}
.track i{position:absolute;left:222px;top:0;width:223px;height:4px;background:var(--orange);border-radius:2px}

.asked{top:1917px;left:117px;width:966px}
.mini-row{position:absolute;top:88px;display:flex;gap:24px}
.mini{width:141px;height:259px;background:var(--white);border:1px solid var(--line);border-radius:8px;box-shadow:0 2px 6px rgba(0,0,0,.06);overflow:hidden;position:relative}
.mini .ph{height:123px}
.mini .body{padding:8px 9px}
.mini h5{font-size:11px;font-weight:700;line-height:15px}
.mini .stars{font-size:10px}
.mini .desc{font-size:6px;color:#666;line-height:8px;margin-top:2px}
.mini .price{position:absolute;left:9px;bottom:32px;font-size:12px}
.mini .btn{position:absolute;right:8px;bottom:8px;width:68px;height:18px;font-size:7px}

.usps{top:2327px;left:117px;width:966px;height:119px;border:1.5px solid #e3c6a2;border-radius:12px;background:#fffaf4;display:flex;padding:18px 16px 0}
.usp{flex:1}
.usp svg{display:block}
.usp h6{font-size:12px;font-weight:700;margin-top:8px}
.usp p{font-size:9px;color:#555;line-height:12px;margin-top:6px;width:200px}

.blogs{top:2490px;left:117px;width:966px}
.blog-row{position:absolute;top:88px;display:flex;gap:14px}
.blog{width:312px;height:293px;background:var(--white);border-radius:10px;box-shadow:0 3px 10px rgba(0,0,0,.1);overflow:hidden;position:relative}
.blog .ph{height:138px}
.blog h4{font-size:13px;font-weight:700;margin:12px 16px 0}
.tags{display:flex;gap:5px;margin:10px 16px 0}
.tag{font-size:7px;font-weight:700;color:var(--white);padding:3px 10px;border-radius:999px}
.blog p{font-size:9px;line-height:12px;color:#555;margin:10px 16px 0}
.blog .more{position:absolute;right:16px;bottom:18px;font-size:10px;color:var(--orange);text-decoration:underline;display:flex;gap:5px;align-items:center}

.news{top:2932px;left:117px;width:966px;height:290px;background:var(--lav);border:1px solid var(--lav-line);border-radius:10px}
.news-left{position:absolute;left:37px;top:58px;width:460px}
.news-left .kicker{font-size:15px;font-weight:600}
.news-left h2{font-size:30px;font-weight:800;line-height:42px;margin-top:8px}
.news-left p{font-size:11px;line-height:16px;margin-top:10px}
.news-right{position:absolute;left:574px;top:58px;width:356px}
.news-right h3{font-size:17px;font-weight:700}
.field{margin-top:16px;height:37px;border-radius:999px;background:var(--white);font-size:11px;color:#999;padding-left:16px;line-height:37px;position:relative}
.field + .field{margin-top:18px}
.field svg{position:absolute;right:16px;top:15px}
.news-right .btn{position:absolute;left:203px;top:196px;width:152px;height:36px;font-size:13px}

.footer{top:3300px;left:0;width:1200px;height:513px;background:var(--peach)}
.fcol{position:absolute;top:70px}
.fcol h5{font-size:14px;font-weight:700;margin-bottom:14px}
.fcol a{display:block;font-size:13px;line-height:28px}
.fnews{position:absolute;left:825px;top:70px;width:270px}
.fnews h5{font-size:17px;font-weight:800}
.fnews p{font-size:11px;margin-top:6px}
.fnews .btn{margin-top:20px;width:110px;height:34px;font-size:13px}
.socials{display:flex;gap:28px;margin-top:30px}
.socials i{width:14px;height:14px;border-radius:50%;background:var(--orange);display:block}
.footer .logo{position:absolute;left:125px;top:380px;font-size:66px;gap:12px;line-height:1}
.footer .logo .dot{width:58px;height:58px}
.legal{position:absolute;right:117px;top:426px;font-size:11px;display:flex;gap:20px;white-space:nowrap}
.legal a{text-decoration:underline}
</style>
</head>
<body>

<div class="abs topbar">Gratis standaard verzending bij bestellingen boven €65</div>

<header class="abs header">
  <div class="logo"><span class="dot"></span>Brenvik</div>
  <div class="search">What are you looking for....
    <svg width="18" height="18" viewBox="0 0 24 24" fill="none" stroke="#f7a441" stroke-width="2.4"><circle cx="10" cy="10" r="7"/><path d="M15 15l6 6"/></svg>
  </div>
  <div class="hicons">
    <div class="hicon"><svg width="18" height="18" viewBox="0 0 24 24" fill="none" stroke="#3c3c3b" stroke-width="2"><path d="M12 22s7-7 7-12a7 7 0 0 0-14 0c0 5 7 12 7 12z"/><circle cx="12" cy="10" r="2.5"/></svg>Stores</div>
    <div class="hicon"><svg width="18" height="18" viewBox="0 0 24 24" fill="none" stroke="#3c3c3b" stroke-width="2"><circle cx="12" cy="12" r="9"/><circle cx="12" cy="10" r="3"/><path d="M6.5 18.5c3-3 8-3 11 0"/></svg>My Account</div>
    <div class="hicon"><svg width="18" height="18" viewBox="0 0 24 24" fill="none" stroke="#3c3c3b" stroke-width="2"><path d="M2 3h3l3 12h11l2-8H7"/><circle cx="9" cy="20" r="1.5"/><circle cx="18" cy="20" r="1.5"/></svg>Cart</div>
  </div>
  <nav class="nav">
    <a style="left:0">Home</a>
    <a style="left:77px">Vissenvoer</a>
    <a style="left:185px">Kippenvoer</a>
    <a style="left:296px">Accessoires</a>
    <a style="left:408px">Contact</a>
    <a style="left:497px;color:var(--red)">Aanbiedingen</a>
  </nav>
  <a class="btn shop">Shop Nu</a>
</header>

<section class="abs hero">
  <div class="hero-card">
    <div class="hero-stripe"></div>
    <div class="hero-img ph" role="img" aria-label="Productfoto van visvoerverpakkingen met tropische vissen"></div>
    <div class="hero-band"><span>12% Korting</span></div>
    <div class="hero-text">
      <span class="badge">premium Nutrition</span>
      <h1>Het Geheim van Gezonde Vissen Begint Hier.</h1>
      <p>Ontdek ons premium voer dat rijk is aan essentiële voedingsstoffen en vitaminen.</p>
      <a class="btn">Shop Nu</a>
    </div>
  </div>
  <div class="dots"><i></i><i class="on"></i><i></i><i></i><i></i></div>
</section>

<section class="abs cats">
  <div class="cats-head">
    <h2 class="sec-title">Vind het Perfecte Voer</h2>
    <p class="sec-sub">Ontdek ons complete aanbod van voeding en essentiële benodigdheden voor blije dieren.</p>
  </div>
  <div class="cat-row">
    <div class="cat">
      <div class="ph" role="img" aria-label="Illustratie van een oranje vis in blauwgroen water" style="background:linear-gradient(180deg,#2f8d92,#4aa9a5)"></div>
      <h3>Visvoer &amp; Supplementen</h3>
      <p>Groeimixen, vlokken, korrels en helderwater-oplossingen.</p>
      <a class="btn-outline">Bekijk Visvoer</a>
    </div>
    <div class="cat">
      <div class="ph" role="img" aria-label="Illustratie van een kip tussen graanhalmen" style="background:linear-gradient(180deg,#d9c7a4,#c9b185)"></div>
      <h3>Kippenvoer: Leg &amp; Meer</h3>
      <p>Non-GMO, biologische en startmixen, direct leverbaar.</p>
      <a class="btn-outline">Bekijk Kippenvoer</a>
    </div>
    <div class="cat">
      <div class="ph" role="img" aria-label="Foto van voerbakken, netten en verzorgingsproducten" style="background:linear-gradient(180deg,#2e2f33,#4a4c52)"></div>
      <h3>Voerbakken, Tools &amp; Basis</h3>
      <p>Blader door automatische feeders, scheppen en benodigdheden.</p>
      <a class="btn-outline">Bekijk Visvoer</a>
    </div>
  </div>
</section>

<section class="abs bundles">
  <h2 class="sec-title">Complete Kits en Bundels</h2>
  <a class="see-all" style="top:6px">Bekijk alle bundels <svg width="14" height="10" viewBox="0 0 14 10" fill="none" stroke="#3c3c3b" stroke-width="1.5"><path d="M0 5h12M8 1l4 4-4 4"/></svg></a>
  <div class="bundle-row">
    <div class="bundle b1">
      <h3>Aquarium Basis Startpakket</h3>
      <p>Alles voor een gezonde, levendige start in het water.</p>
      <div class="ph" role="img" aria-label="Productfoto van aquariumvoer en waterbehandelingsflessen" style="background:linear-gradient(135deg,#f6cf9d,#e9b57a)"></div>
      <span class="go"><svg width="16" height="16" viewBox="0 0 16 16" fill="none" stroke="#fff" stroke-width="2"><path d="M2 8h11M9 4l4 4-4 4"/></svg></span>
    </div>
    <div class="bundle b2">
      <h3>Hok Verdediging Basis</h3>
      <p>Essentiële, niet-giftige oplossingen voor hygiëne en ongediertebestrijding.</p>
      <div class="ph" role="img" aria-label="Productfoto van sprayfles en hokverzorging" style="background:linear-gradient(135deg,#d3dbe1,#c5ccd2)"></div>
      <span class="go"><svg width="16" height="16" viewBox="0 0 16 16" fill="none" stroke="#fff" stroke-width="2"><path d="M2 8h11M9 4l4 4-4 4"/></svg></span>
    </div>
    <div class="bundle b3">
      <h3>Maximale Legprestatie Kit</h3>
      <p>Topsupplementen voor optimale hengezondheid en legkwaliteit.</p>
      <div class="ph" role="img" aria-label="Productfoto van legvoer en supplementen met eieren" style="background:linear-gradient(135deg,#d6e7c4,#c9b78f)"></div>
      <span class="go"><svg width="16" height="16" viewBox="0 0 16 16" fill="none" stroke="#fff" stroke-width="2"><path d="M2 8h11M9 4l4 4-4 4"/></svg></span>
    </div>
  </div>
</section>

<section class="abs rated">
  <div class="rated-in">
    <h2 class="sec-title">Best beoordeelde producten voor vis- en kippenvoer</h2>
    <a class="see-all" style="top:6px">Bekijk alle bundels <svg width="14" height="10" viewBox="0 0 14 10" fill="none" stroke="#3c3c3b" stroke-width="1.5"><path d="M0 5h12M8 1l4 4-4 4"/></svg></a>
    <div class="prod-row">
      <div class="prod">
        <div class="ph" role="img" aria-label="Productfoto van legvoerverpakking met eieren op houten tafel" style="background:linear-gradient(180deg,#efe7dc,#b98f62)"></div>
        <span class="badge">premium Nutrition</span>
        <div class="body">
          <h4>Marevo Groeivlokken — 400g</h4>
          <div class="stars">★★★★☆<small>24 reviews</small></div>
          <p class="desc">Eiwitrijke vlokken voor tropische gezelschapsvissen.</p>
        </div>
        <div class="price">€9.95<small>(incl. BTW)</small></div>
        <a class="btn">In Winkelwagen</a>
      </div>
      <div class="prod">
        <div class="ph" role="img" aria-label="Productfoto van sprayfles en zakken hokverzorging" style="background:linear-gradient(180deg,#f4f4f4,#e2e6e8)"></div>
        <div class="body">
          <h4>Klaroma Bio-Koolstof — 500g</h4>
          <div class="stars">★★★★☆<small>24 reviews</small></div>
          <p class="desc">Geactiveerde koolstof voor kristalhelder, geurvrij water.</p>
        </div>
        <div class="price">€14.50<small>(incl. BTW)</small></div>
        <a class="btn">In Winkelwagen</a>
      </div>
      <div class="prod">
        <div class="ph" role="img" aria-label="Productfoto van aquariumvoer en flessen waterbehandeling" style="background:linear-gradient(180deg,#f3f3f3,#dfe6ea)"></div>
        <span class="badge" style="background:var(--red)">premium Nutrition</span>
        <div class="body">
          <h4>Hofvelde Legkorrels — 10kg</h4>
          <div class="stars">★★★★☆<small>24 reviews</small></div>
          <p class="desc">Complete, GGO-vrije voeding voor sterke eierschalen en rijke dooiers.</p>
        </div>
        <div class="price">€24.99<small>(incl. BTW)</small></div>
        <a class="btn">In Winkelwagen</a>
      </div>
      <div class="prod">
        <div class="ph" role="img" aria-label="Productfoto van visvoerzakken en losse vlokken" style="background:linear-gradient(180deg,#e9eef0,#cfd8dc)"></div>
        <div class="body">
          <h4>Dryhold Voerautomaat — 5kg Capaciteit</h4>
          <div class="stars">★★★★☆<small>24 reviews</small></div>
          <p class="desc">Houdt voer droog, minder verspilling.</p>
        </div>
        <div class="price">€39.00<small>(incl. BTW)</small></div>
        <a class="btn">In Winkelwagen</a>
      </div>
    </div>
  </div>
  <span class="arrow-btn" style="left:57px;top:472px"><svg width="16" height="16" viewBox="0 0 16 16" fill="none" stroke="#fff" stroke-width="2"><path d="M14 8H3M7 4L3 8l4 4"/></svg></span>
  <span class="arrow-btn" style="left:1103px;top:472px"><svg width="16" height="16" viewBox="0 0 16 16" fill="none" stroke="#fff" stroke-width="2"><path d="M2 8h11M9 4l4 4-4 4"/></svg></span>
  <div class="track"><i></i></div>
</section>

<section class="abs asked">
  <h2 class="sec-title">Meest Gevraagd</h2>
  <p class="sec-sub">Dit zijn de snelst verkopende items van dit moment.</p>
  <div class="mini-row">
    <div class="mini"><div class="ph" role="img" aria-label="Productfoto aquariumvoer en flessen" style="background:linear-gradient(180deg,#f5f5f5,#e3e8ea)"></div><div class="body"><h5>Dryhold Voerautomaat — 5kg Capaciteit</h5><div class="stars">★★★★☆<small>24 reviews</small></div><p class="desc">Houdt voer droog en minimaliseert verspilling in alle weersomstandigheden.</p></div><div class="price">€39.00<small>(incl. BTW)</small></div><a class="btn">In Winkelwagen</a></div>
    <div class="mini"><div class="ph" role="img" aria-label="Productfoto rode snoeischaar" style="background:linear-gradient(180deg,#fafafa,#eeeeee)"></div><div class="body"><h5>Dryhold Voerautomaat — 5kg Capaciteit</h5><div class="stars">★★★★☆<small>24 reviews</small></div><p class="desc">Houdt voer droog en minimaliseert verspilling in alle weersomstandigheden.</p></div><div class="price">€39.00<small>(incl. BTW)</small></div><a class="btn">In Winkelwagen</a></div>
    <div class="mini"><div class="ph" role="img" aria-label="Productfoto sprayfles en hokverzorging" style="background:linear-gradient(180deg,#f7f5f2,#e8e2da)"></div><div class="body"><h5>Dryhold Voerautomaat — 5kg Capaciteit</h5><div class="stars">★★★★☆<small>24 reviews</small></div><p class="desc">Houdt voer droog en minimaliseert verspilling in alle weersomstandigheden.</p></div><div class="price">€39.00<small>(incl. BTW)</small></div><a class="btn">In Winkelwagen</a></div>
    <div class="mini"><div class="ph" role="img" aria-label="Productfoto metalen voerschep" style="background:linear-gradient(180deg,#fafafa,#ececec)"></div><div class="body"><h5>Dryhold Voerautomaat — 5kg Capaciteit</h5><div class="stars">★★★★☆<small>24 reviews</small></div><p class="desc">Houdt voer droog en minimaliseert verspilling in alle weersomstandigheden.</p></div><div class="price">€39.00<small>(incl. BTW)</small></div><a class="btn">In Winkelwagen</a></div>
    <div class="mini"><div class="ph" role="img" aria-label="Productfoto visnetje" style="background:linear-gradient(180deg,#fafafa,#eeeeee)"></div><div class="body"><h5>Dryhold Voerautomaat — 5kg Capaciteit</h5><div class="stars">★★★★☆<small>24 reviews</small></div><p class="desc">Houdt voer droog en minimaliseert verspilling in alle weersomstandigheden.</p></div><div class="price">€39.00<small>(incl. BTW)</small></div><a class="btn">In Winkelwagen</a></div>
    <div class="mini"><div class="ph" role="img" aria-label="Productfoto visvoerzakken" style="background:linear-gradient(180deg,#e9eef0,#cfd8dc)"></div><div class="body"><h5>Dryhold Voerautomaat — 5kg Capaciteit</h5><div class="stars">★★★★☆<small>24 reviews</small></div><p class="desc">Houdt voer droog en minimaliseert verspilling in alle weersomstandigheden.</p></div><div class="price">€39.00<small>(incl. BTW)</small></div><a class="btn">In Winkelwagen</a></div>
  </div>
</section>

<section class="abs usps">
  <div class="usp">
    <svg width="24" height="24" viewBox="0 0 24 24" fill="none" stroke="#3c3c3b" stroke-width="2"><path d="M4 12l5 5L20 6"/></svg>
    <h6>Voer van Premium Kwaliteit</h6>
    <p>Vers verpakt en snel geleverd. Uw bestelling arriveert in perfecte staat.</p>
  </div>
  <div class="usp">
    <svg width="26" height="24" viewBox="0 0 26 24" fill="none" stroke="#3c3c3b" stroke-width="2"><rect x="2" y="6" width="13" height="10" fill="#e5482b"/><path d="M15 9h5l4 4v3h-9z"/><circle cx="7" cy="18" r="2" fill="#fff"/><circle cx="19" cy="18" r="2" fill="#fff"/></svg>
    <h6>Snelle &amp; Betrouwbare Levering</h6>
    <p>Vers verpakt en snel geleverd. Uw bestelling arriveert in perfecte staat.</p>
  </div>
  <div class="usp">
    <svg width="24" height="24" viewBox="0 0 24 24" fill="none" stroke="#3c3c3b" stroke-width="2"><circle cx="12" cy="8" r="4" fill="#f7a441"/><path d="M4 21c1-5 15-5 16 0" fill="#3fa33a"/></svg>
    <h6>Vertrouwd door Dierenliefhebbers</h6>
    <p>Duizenden fokkers en hobbyisten vertrouwen op onze bewezen resultaten.</p>
  </div>
  <div class="usp">
    <svg width="24" height="24" viewBox="0 0 24 24" fill="none" stroke="#3c3c3b" stroke-width="2"><circle cx="12" cy="10" r="7" fill="#e5482b"/><path d="M8 16l-2 6 6-3 6 3-2-6"/></svg>
    <h6>Tevredenheid Gegarandeerd</h6>
    <p>Tevredenheid gegarandeerd. Bent u niet tevreden? Dan zijn wij het ook niet.</p>
  </div>
</section>

<section class="abs blogs">
  <h2 class="sec-title">Kenniscentrum &amp; Blogs</h2>
  <p class="sec-sub">Expert tips, onderhoudsgidsen en nieuws voor elke vis- en kippenhouder.</p>
  <div class="blog-row">
    <div class="blog">
      <div class="ph" role="img" aria-label="Foto van een verlicht aquarium met koraal op een bureau" style="background:linear-gradient(180deg,#c9d3db,#2a5fb4 60%,#6e6f73)"></div>
      <h4>De Basis: Je Aquarium Succesvol Indraaien</h4>
      <div class="tags"><span class="tag" style="background:var(--green)">Beginnersgids</span><span class="tag" style="background:var(--blue)">Waterkwaliteit</span></div>
      <p>De belangrijkste stap voor elke nieuwe aquariaan. Leer de cruciale stappen voor het opbouwen van gezonde bacteriën. Voorkom beginnersfouten en creëer direct een veilige omgeving voor uw vissen.</p>
      <a class="more">Bekijk alle bundels <svg width="12" height="9" viewBox="0 0 14 10" fill="none" stroke="#f7a441" stroke-width="1.5"><path d="M0 5h12M8 1l4 4-4 4"/></svg></a>
    </div>
    <div class="blog">
      <div class="ph" role="img" aria-label="Foto van kippen in het gras" style="background:linear-gradient(180deg,#6b8f3a,#a2582b 55%,#5c7d2e)"></div>
      <h4>Waarom Eiwitten Nu Cruciaal Zijn</h4>
      <div class="tags"><span class="tag" style="background:var(--red)">Kippengezondheid</span><span class="tag" style="background:var(--orange)">Voeding</span></div>
      <p>De rui vraagt veel van uw kippen. Begrijp welke voeding en supplementen het verenkleed herstel versnellen en de leg snel weer op gang brengen.</p>
      <a class="more">Bekijk alle bundels <svg width="12" height="9" viewBox="0 0 14 10" fill="none" stroke="#f7a441" stroke-width="1.5"><path d="M0 5h12M8 1l4 4-4 4"/></svg></a>
    </div>
    <div class="blog">
      <div class="ph" role="img" aria-label="Foto van een beplant aquarium onder kleurrijke LED-verlichting" style="background:linear-gradient(180deg,#6a2fa8,#1d6b3a 60%,#15301f)"></div>
      <h4>De Juiste LED's voor Waterplanten</h4>
      <div class="tags"><span class="tag" style="background:var(--green)">Planten</span><span class="tag" style="background:var(--blue)">Aquariumtechniek</span></div>
      <p>Een diepe duik in PAR, Kelvin en lumen. Ontdek hoe u uw verlichting instelt voor maximale plantengroei en om de levendige kleuren van uw vissen te accentueren.</p>
      <a class="more">Bekijk alle bundels <svg width="12" height="9" viewBox="0 0 14 10" fill="none" stroke="#f7a441" stroke-width="1.5"><path d="M0 5h12M8 1l4 4-4 4"/></svg></a>
    </div>
  </div>
</section>

<section class="abs news">
  <div class="news-left">
    <p class="kicker">Onze nieuwsbrief</p>
    <h2>Blijf op de hoogte met onze wekelijkse nieuwsbrief</h2>
    <p>Ontvang exclusieve tips van onze dierenexperts direct in uw inbox. Wees de eerste die nieuwe producten en speciale kortingen ontdekt. Content op maat, gesegmenteerd voor uw vissen of kippen.</p>
  </div>
  <div class="news-right">
    <h3>Aanmelden voor nieuwsbrief</h3>
    <div class="field">Je e-mailadres</div>
    <div class="field">Je diersoort<svg width="10" height="7" viewBox="0 0 10 7" fill="none" stroke="#f7a441" stroke-width="1.6"><path d="M1 1l4 4 4-4"/></svg></div>
    <a class="btn">Meld je nu aan</a>
  </div>
</section>

<footer class="abs footer">
  <div class="fcol" style="left:117px">
    <h5>Klantenservice</h5>
    <a>Veelgestelde Vragen</a><a>Verzending &amp; Levering</a><a>Retourneren &amp; Ruilen</a><a>Bestelstatus</a><a>Contact</a><a>Garantie &amp; Service</a><a>Account Beheren</a><a>Betaalmethoden</a>
  </div>
  <div class="fcol" style="left:353px">
    <h5>Over Ons</h5>
    <a>Ons Verhaal</a><a>Vacatures</a><a>Algemene Voorwaarden</a><a>Privacybeleid</a><a>Cookiebeleid</a><a>Pers &amp; Media</a><a>Algemene Voorwaarden</a><a>Onze Missie</a><a>Duurzaamheid</a>
  </div>
  <div class="fcol" style="left:599px">
    <h5>Ontdekken</h5>
    <a>Alles voor Vissen</a><a>Alles voor Kippen</a><a>Bestsellers</a><a>Nieuw in Assortiment</a><a>enniscentrum &amp; Blogs</a><a>Alle Merken</a><a>Productgidsen</a>
  </div>
  <div class="fnews">
    <h5>Aanmelden voor nieuwsbrief</h5>
    <p>Blijf op de Hoogte met Nieuws &amp; Tips</p>
    <a class="btn">Meld je nu aan</a>
    <div class="socials"><i></i><i></i><i></i><i></i></div>
  </div>
  <div class="logo"><span class="dot"></span>Brenvik</div>
  <div class="legal"><span>© 2025 Brenvik. Alle rechten voorbehouden</span><a>Privacybeleid</a><a>Cookiebeleid</a><a>Algemene Voorwaarden</a></div>
</footer>

</body>
</html>
```